Northern Terrain Published Photographer Website

I need a website to feature a home page slide show of 6 of my top photos then a few simple pages including; gallery, bio, social, checkout, services
Updates

Need extra days to review

Target Market(s)

photography

Industry/Entity Type

Photographer

Coding

Coded - Design and coding required

Number of Pages Required

5+ page

Colors

Designer to choose colors to be used in the design.

Requirements
Must have
• clean eye catching elegant trendy
Nice to have
• unique and creative from other photographer websites

```html
<!DOCTYPE html>
<html lang="en">
<head>
<meta charset="utf-8">
<title>Northern Terrain Photography</title>
<link href="https://fonts.googleapis.com/css2?family=Oswald:wght@600&family=Poppins:wght@400;500&family=Ubuntu:wght@400;500&display=swap" rel="stylesheet">
<style>
:root{
  --gold:#ffc107;
  --gold-bright:#ffd21a;
  --header:#a8901c;
  --ink:#000000;
  --white:#ffffff;
  --muted:#bdbdbd;
  --rule:#8a8a8a;
  --rule-light:#e8d9a8;
}
html,body{margin:0;padding:0;background:var(--ink);}
body{width:1200px;height:3103px;overflow:hidden;position:relative;font-family:'Poppins',sans-serif;color:var(--white);}
.backdrop{position:absolute;left:0;top:0;width:1200px;height:3103px;}
.site-header{position:absolute;left:0;top:0;width:1200px;height:83px;background:var(--header);opacity:.95;}
.brand{position:absolute;display:flex;align-items:center;gap:10px;font-family:'Poppins',sans-serif;font-weight:500;font-size:24px;color:var(--white);}
.brand-dot{width:14px;height:14px;border-radius:50%;background:var(--white);}
.site-header .brand{left:114px;top:24px;}
.main-nav{position:absolute;top:31px;left:0;width:1200px;font-size:14px;}
.main-nav a{position:absolute;color:var(--white);text-decoration:none;}
.nav-cta{position:absolute;left:981px;top:26px;width:105px;height:31px;background:var(--gold);color:var(--white);font-size:14px;display:flex;align-items:center;justify-content:center;}
.hero-title{position:absolute;left:534px;top:322px;font-family:'Oswald',sans-serif;font-weight:600;font-size:32px;color:var(--gold);line-height:1;}
.hero-sub{position:absolute;left:475px;top:366px;font-size:22px;letter-spacing:8px;color:var(--white);}
.hero-text{position:absolute;left:370px;top:392px;width:460px;text-align:center;font-size:11px;line-height:18px;color:var(--white);}
.section-title{position:absolute;font-family:'Ubuntu',sans-serif;font-size:40px;line-height:1;color:var(--white);}
.section-title .initial{color:var(--gold);font-size:50px;}
.section-title.on-gold .initial{color:var(--gold-bright);}
.section-sub{position:absolute;font-family:'Ubuntu',sans-serif;font-size:21px;letter-spacing:6px;color:var(--white);}
.section-rule{position:absolute;height:2px;width:230px;background:var(--rule);}
.section-rule.on-gold{background:var(--rule-light);width:190px;}
.photo{position:absolute;}
.photo-mark{position:absolute;width:20px;height:20px;background:var(--white);}
.footer-nav{position:absolute;top:3023px;left:0;width:1200px;font-size:13px;}
.footer-nav a{position:absolute;color:var(--white);text-decoration:none;}
.footer-rule{position:absolute;left:0;top:2994px;width:1200px;height:1px;background:#2a2a2a;}
.copyright{position:absolute;left:0;top:3056px;width:1200px;text-align:center;font-size:11px;color:var(--muted);}
.social{position:absolute;width:38px;height:38px;border:2px solid var(--white);border-radius:50%;box-sizing:border-box;top:2909px;}
</style>
</head>
<body>

<svg class="backdrop" width="1200" height="3103" viewBox="0 0 1200 3103">
  <defs>
    <linearGradient id="heroTone" x1="0" y1="0" x2="0" y2="1">
      <stop offset="0" stop-color="#1d2a1c"/><stop offset=".5" stop-color="#2d2f2a"/><stop offset="1" stop-color="#4b4842"/>
    </linearGradient>
    <linearGradient id="natureTone" x1="0" y1="0" x2="0" y2="1">
      <stop offset="0" stop-color="#c4961a"/><stop offset=".35" stop-color="#b88a14"/><stop offset=".7" stop-color="#a97c12"/><stop offset="1" stop-color="#c49628"/>
    </linearGradient>
    <linearGradient id="sunriseTone" x1="0" y1="0" x2="0" y2="1">
      <stop offset="0" stop-color="#2a2d2c"/><stop offset=".45" stop-color="#3d4a34"/><stop offset="1" stop-color="#35452a"/>
    </linearGradient>
    <linearGradient id="sunsetTone" x1="0" y1="0" x2="0" y2="1">
      <stop offset="0" stop-color="#c6520c"/><stop offset=".5" stop-color="#b5510a"/><stop offset="1" stop-color="#8f3c08"/>
    </linearGradient>
    <linearGradient id="canyonTone" x1="0" y1="0" x2="0" y2="1">
      <stop offset="0" stop-color="#3a3f48"/><stop offset=".5" stop-color="#4a3a2e"/><stop offset="1" stop-color="#2d3633"/>
    </linearGradient>
  </defs>
  <g role="img" aria-label="Vintage camera resting on the forest floor">
    <path d="M0 0H1200V628C900 630 700 620 650 645C610 668 590 668 550 645C500 620 300 630 0 628Z" fill="url(#heroTone)"/>
  </g>
  <g role="img" aria-label="Golden desert canyon with a crystal ball">
    <path d="M0 1078C300 1040 560 1022 800 1028C1000 1034 1120 1050 1200 1068V3103H0Z" fill="url(#natureTone)"/>
  </g>
  <g role="img" aria-label="Green hills at dusk">
    <path d="M0 1484C400 1440 800 1430 1200 1450V3103H0Z" fill="url(#sunriseTone)"/>
  </g>
  <g role="img" aria-label="Pier posts in an orange sunset lake">
    <path d="M0 1912C400 1868 800 1862 1200 1905V3103H0Z" fill="url(#sunsetTone)"/>
  </g>
  <g role="img" aria-label="River canyon at twilight">
    <path d="M0 2358C300 2290 700 2250 1200 2350V3103H0Z" fill="url(#canyonTone)"/>
  </g>
  <path d="M0 2830H470C540 2830 560 2868 600 2868C640 2868 660 2830 730 2830H1200V3103H0Z" fill="var(--ink)"/>
</svg>

<header class="site-header">
  <div class="brand"><span>Lena Marlowe</span><span class="brand-dot"></span></div>
  <nav class="main-nav">
    <a style="left:585px">Home</a>
    <a style="left:664px">Bio</a>
    <a style="left:720px">Gallery</a>
    <a style="left:798px">Services</a>
    <a style="left:897px">Contact</a>
  </nav>
  <a class="nav-cta">Contact</a>
</header>

<div class="photo" role="img" aria-label="Vintage film camera" style="left:268px;top:272px;width:350px;height:255px;background:radial-gradient(ellipse at 45% 40%,#5e5e5a,#2b2b29 70%);border-radius:14px;opacity:.8;"></div>
<div class="hero-title">Northern Terrain</div>
<div class="hero-sub">PHOTOGRAPHY</div>
<p class="hero-text">Lorem ipsum dolor sit amet, consectetuer adipiscing elit, sed diam nonummy nibh euismod tincidunt.</p>

<!-- Wild life -->
<div class="photo" role="img" aria-label="Tiger lying down" style="left:830px;top:664px;width:370px;height:362px;background:radial-gradient(ellipse at 50% 40%,#d88a36,#8a4818 35%,#3a1e0c 60%,#000 78%);"></div>
<div class="photo" role="img" aria-label="Deer grazing in dry grass" style="left:592px;top:735px;width:240px;height:213px;background:radial-gradient(ellipse at 45% 40%,#8a7a62,#5a4a38 60%,#3e3226);"></div>
<div class="photo-mark" style="left:808px;top:924px;"></div>
<div class="section-title" style="left:394px;top:774px;"><span class="initial">W</span>ild life</div>
<div class="section-sub" style="left:428px;top:828px;">Photography</div>
<div class="section-rule" style="left:394px;top:862px;"></div>

<!-- Nature -->
<div class="photo" role="img" aria-label="Red rock butte reflected in water" style="left:304px;top:1148px;width:240px;height:214px;background:linear-gradient(180deg,#4fa0a8 0,#c98a3a 35%,#b8743a 50%,#d8a25a 70%,#4f8c94 100%);"></div>
<div class="section-title on-gold" style="left:588px;top:1184px;"><span class="initial">N</span>ature</div>
<div class="section-sub" style="left:530px;top:1238px;">Photography</div>
<div class="section-rule on-gold" style="left:530px;top:1272px;"></div>

<!-- Sunrise -->
<div class="photo" role="img" aria-label="Sun rising over a lake" style="left:565px;top:1544px;width:238px;height:215px;background:radial-gradient(ellipse at 50% 52%,#fff4c8,#f0a030 25%,#9a4a18 60%,#5a2a12);"></div>
<div class="photo-mark" style="left:782px;top:1738px;"></div>
<div class="section-title" style="left:370px;top:1586px;"><span class="initial">S</span>unrise</div>
<div class="section-sub" style="left:400px;top:1640px;">Photography</div>
<div class="section-rule" style="left:370px;top:1674px;"></div>

<!-- Sunset -->
<div class="photo" role="img" aria-label="Desert tree silhouetted against a purple sunset" style="left:304px;top:1957px;width:240px;height:214px;background:radial-gradient(ellipse at 50% 45%,#f4c0a0,#c85a8a 35%,#6a2a7a 70%,#2a1030);"></div>
<div class="section-title" style="left:572px;top:2016px;"><span class="initial">S</span>unset</div>
<div class="section-sub" style="left:520px;top:2070px;">Photography</div>
<div class="section-rule" style="left:520px;top:2104px;"></div>

<!-- Gallery strip -->
<div class="photo" role="img" aria-label="River bend in a red canyon" style="left:0;top:2406px;width:219px;height:284px;background:linear-gradient(180deg,#d9c4a0 0,#b06a3a 35%,#3a6a60 65%,#7a4a2a 100%);"></div>
<div class="photo" role="img" aria-label="Crystal ball on a beach at dusk" style="left:219px;top:2386px;width:226px;height:324px;background:radial-gradient(circle at 50% 50%,#c8b4f0,#8a6ac8 35%,#4a3a8a 100%);"></div>
<div class="photo" role="img" aria-label="Portrait of the photographer" style="left:445px;top:2365px;width:308px;height:368px;background:linear-gradient(180deg,#fafafa 0,#eae4d8 60%,#8a8a8a 100%);"></div>
<div class="photo" role="img" aria-label="Waterfall under an arched bridge in autumn" style="left:753px;top:2386px;width:226px;height:324px;background:linear-gradient(180deg,#f2f2ee 0,#b8a060 40%,#7a8a70 75%,#d8c890 100%);"></div>
<div class="photo" role="img" aria-label="Red rock butte reflected in water" style="left:979px;top:2406px;width:221px;height:284px;background:linear-gradient(180deg,#5aa8b0 0,#d89a4a 40%,#c8843a 60%,#4a8a90 100%);"></div>

<!-- Footer -->
<footer>
  <div class="brand" style="left:114px;top:2912px;"><span>Lena Marlowe</span><span class="brand-dot"></span></div>
  <span class="social" style="left:871px;"></span>
  <span class="social" style="left:929px;"></span>
  <span class="social" style="left:989px;"></span>
  <span class="social" style="left:1047px;"></span>
  <div class="footer-rule"></div>
  <nav class="footer-nav">
    <a style="left:418px">Home</a>
    <a style="left:496px">Bio</a>
    <a style="left:554px">Gallery</a>
    <a style="left:630px">Services</a>
    <a style="left:731px">Contact</a>
  </nav>
  <div class="copyright">© All Rights Reserved 2019.</div>
</footer>

</body>
</html>
```